Wound Care Flyer

Looking for a Trifold brochure that is modern and has a high aesthetic. (Specialty services) Would like the colors to center around Black and Gold. Possibly updating the logo. Attached is the old brochure and a document about our services.

```html
<!DOCTYPE html>
<html lang="en">
<head>
<meta charset="utf-8">
<title>Harbor Lane Care – Trifold Brochure</title>
<link href="https://fonts.googleapis.com/css2?family=Lato:ital,wght@0,300;0,400;0,700;0,900;1,300;1,400;1,700&display=swap" rel="stylesheet">
<style>
:root{
  --bg:#ececec;
  --black:#050505;
  --gold:#c9a46a;
  --gold-light:#f1dcb3;
  --gold-deep:#8a5a30;
  --copper:#7a4a25;
  --white:#ffffff;
  --text-light:#e6e6e6;
  --ink:#1a1208;
}
*{margin:0;padding:0;box-sizing:border-box}
html,body{width:1200px;height:1200px;overflow:hidden;background:var(--bg);font-family:'Lato',sans-serif}
.sheet{position:absolute;width:695px;height:537px;background:var(--black);box-shadow:4px 5px 8px rgba(0,0,0,.35);overflow:hidden}
.sheet--outside{left:119px;top:57px}
.sheet--inside{left:352px;top:623px}
.panel{position:absolute;top:0;width:232px;height:537px}
.p1{left:0}.p2{left:232px}.p3{left:464px;width:231px}
.abs{position:absolute}
.center{text-align:center}

/* outside, panel 1 */
.partner-title{top:30px;left:0;width:232px;font-size:18px;line-height:21px;color:var(--gold);font-weight:400}
.benefit{position:absolute;left:27px;width:180px;height:88px;border:1px solid var(--gold);border-radius:10px 22px 6px 14px;background:linear-gradient(135deg,#2a2a2a 0%,#0a0a0a 45%,#000 70%,#3a3a3a 100%);text-align:center;padding:10px 8px 0;box-shadow:3px 3px 0 #3a2a18}
.benefit h3{font-size:10px;font-weight:700;color:var(--white);line-height:12px;margin-bottom:5px}
.benefit p{font-size:8.3px;font-weight:300;color:var(--text-light);line-height:12.3px}
.bottom-bar{position:absolute;left:0;top:519px;width:695px;height:18px;background:linear-gradient(90deg,var(--gold-light) 0%,var(--gold) 20%,var(--gold-deep) 33%,#111 36%,#000 50%,#111 62%,var(--gold-deep) 67%,var(--copper) 100%)}

/* outside, panel 2 */
.panel-dark{background:linear-gradient(90deg,#000 0%,#1c1c1c 35%,#050505 60%,#1a1a1a 100%)}
.contact-title{top:52px;width:232px;font-size:19px;font-weight:900;color:var(--ink);letter-spacing:.3px}
.contact-line{width:232px;font-size:12.5px;font-weight:700;color:var(--ink);line-height:17.5px}
.icon{position:absolute;left:105px;width:22px;height:22px}

/* brand name */
.brand-name{color:var(--gold);font-weight:400;letter-spacing:.3px;line-height:1.2}

/* outside, panel 3 */
.portrait{left:0;top:185px;width:231px;height:334px}
.name-tag{top:484px;width:231px;font-size:13.5px;font-weight:700;color:var(--gold)}

/* inside */
.p-white{background:var(--white)}
.heading{top:30px;width:232px;font-size:17.5px;line-height:21px;font-weight:900;color:var(--gold)}
.accent-band{position:absolute;left:0;top:95px;width:695px;height:12px;background:linear-gradient(90deg,var(--gold-light) 0%,var(--gold) 30%,#e9dcc9 55%,var(--gold-deep) 70%,var(--copper) 100%)}
.body-copy{font-size:8.3px;line-height:12.3px;font-weight:300;color:var(--text-light)}
.quote-card{left:32px;top:327px;width:178px;height:177px;border-radius:8px 28px 8px 28px;background:linear-gradient(135deg,#3b3b3b 0%,#0d0d0d 35%,#000 60%,#2d2d2d 100%);padding:22px 18px 0;text-align:center;font-size:11.4px;line-height:18.5px;font-style:italic;font-weight:700;color:var(--gold)}
.services-frame{left:14px;top:20px;width:204px;height:496px;border:2px solid var(--gold-deep);border-radius:14px}
.services-title{top:30px;width:232px;font-size:16.5px;line-height:18px;font-weight:900;color:var(--copper)}
.services-intro{left:28px;top:124px;width:180px;font-size:8.3px;line-height:12.3px;color:#444;font-weight:400}
.service-band{position:absolute;left:16px;width:200px;height:22px;background:var(--copper);color:var(--white);font-size:10px;line-height:22px;text-align:center;font-weight:400}
.service-note{position:absolute;left:28px;width:176px;font-size:8.3px;line-height:12.3px;font-style:italic;color:#555;text-align:center}
.treatments{position:absolute;left:30px;top:356px;width:172px;list-style:none}
.treatments li{height:21px;line-height:20px;border-top:1px solid #b89877;font-size:8.3px;font-style:italic;color:var(--copper);text-align:center;font-weight:400}
.treatments li:last-child{border-bottom:1px solid #b89877}
.forest{left:22px;top:248px;width:189px;height:189px;border-radius:50%}
</style>
</head>
<body>

<section class="sheet sheet--outside">
  <div class="panel p1">
    <h2 class="abs center partner-title">Partner with<br>Harbor Lane Care</h2>
    <div class="benefit" style="top:94px"><h3>ENHANCED PATIENT<br>OUTCOMES</h3><p>Our specialized expertise in advanced wound care leads to faster healing times and improved patient satisfaction.</p></div>
    <div class="benefit" style="top:200px"><h3>EXTENDED REACH</h3><p>Our in-home services allow your patients to receive high-quality care without the need for frequent visits, reducing the burden on your resources.</p></div>
    <div class="benefit" style="top:306px"><h3>PROFESSIONAL INTEGRITY</h3><p>As a trusted partner, we uphold the highest standards of care and professionalism, reflecting positively on your clinic's reputation.</p></div>
    <div class="benefit" style="top:413px;height:76px"><h3>SEAMLESS COLLABORATION</h3><p>We maintain open communication with referring clinics, ensuring a coordinated approach to patient care.</p></div>
  </div>

  <div class="panel p2 panel-dark">
    <svg class="abs" style="left:0;top:0" width="232" height="260" viewBox="0 0 232 260" aria-hidden="true">
      <defs>
        <linearGradient id="goldSweep" x1="0" y1="1" x2="1" y2="0">
          <stop offset="0" stop-color="#f3e0b8"/><stop offset=".45" stop-color="#b88a5a"/><stop offset=".8" stop-color="#7d4f2a"/><stop offset="1" stop-color="#b8895c"/>
        </linearGradient>
      </defs>
      <path d="M0 0H232V205Q116 285 0 205Z" fill="#fff"/>
      <path d="M0 0H232V198Q116 268 0 198Z" fill="url(#goldSweep)"/>
    </svg>
    <h2 class="abs center contact-title">CONTACT US</h2>
    <svg class="icon" style="top:83px" viewBox="0 0 22 22" aria-hidden="true"><circle cx="11" cy="11" r="11" fill="#111"/><path d="M7.5 6.5l2 2-1 1.3c.7 1.4 1.8 2.5 3.2 3.2l1.3-1 2 2-1.2 1.5c-3.5-.3-7.4-4.2-7.7-7.7z" fill="none" stroke="#fff" stroke-width=".9"/></svg>
    <p class="abs center contact-line" style="top:108px">O: (555) 014-2208<br>F: (555) 014-2291</p>
    <svg class="icon" style="top:153px" viewBox="0 0 22 22" aria-hidden="true"><circle cx="11" cy="11" r="11" fill="#111"/><rect x="6" y="7.5" width="10" height="7" fill="none" stroke="#fff" stroke-width=".9"/><path d="M6 7.5l5 4 5-4" fill="none" stroke="#fff" stroke-width=".9"/></svg>
    <p class="abs center contact-line" style="top:177px;font-size:12px">harborlanecare@example.com</p>
    <p class="abs center brand-name" style="top:410px;width:232px;font-size:16px">Harbor Lane Care</p>
  </div>

  <div class="panel p3 panel-dark">
    <p class="abs center brand-name" style="top:110px;width:231px;font-size:18px">Harbor Lane Care</p>
    <div class="abs portrait" role="img" aria-label="Portrait photo of the nurse practitioner in a white coat" style="background:radial-gradient(ellipse at 50% 55%,#6a6468 0%,#3a3536 35%,#161414 65%,#0a0a0a 100%)"></div>
    <p class="abs center name-tag">DANA WHITFIELD, FNP-C</p>
  </div>

  <div class="bottom-bar"></div>
</section>

<section class="sheet sheet--inside">
  <div class="panel p1">
    <h2 class="abs center heading">MOBILE<br>WOUND CARE</h2>
    <p class="abs body-copy" style="left:32px;top:124px;width:182px">With a focus on convenience, expertise, and compassion, we bring the highest standard of wound care directly to the patient's home. Working side-by-side with the patient's physician, our team of experienced specialists utilize cutting-edge technology and personalized treatment plans to ensure optimal healing and comfort. From thorough wound assessments to advanced therapies and ongoing support, we prioritize the wellbeing of our patients every step of the way. Whether it's managing chronic wounds, postsurgery recovery, we go above and beyond to provide comprehensive and compassionate care.</p>
    <div class="abs quote-card">With our concierge approach, we aim to make the healing journey as seamless and comfortable as possible, empowering our patients to live their best lives.</div>
  </div>

  <div class="panel p2 p-white">
    <div class="abs services-frame"></div>
    <h2 class="abs center services-title">LEADERS IN<br>MOBILE ADVANCED<br>WOUND CARE</h2>
    <p class="abs services-intro">We provide a complete wound management program for our patients that includes the use of advanced treatments, the creation of care plans, and coordination of care with other clinicians. Our comprehensive in-home wound care services include:</p>
    <div class="service-band" style="top:215px">Advanced Wound Assessment</div>
    <p class="service-note" style="top:242px">Thorough evaluation of wound type, size, and stage to develop a tailored treatment plan.</p>
    <div class="service-band" style="top:297px">Cutting-Edge Treatments</div>
    <p class="service-note" style="top:324px">Utilization of the latest technologies and techniques in wound care, including:</p>
    <ul class="treatments">
      <li>COMPRESSION</li>
      <li>BIOLOGIC SKIN SUBSTITUTES</li>
      <li>NEGATIVE PRESSURE WOUND THERAPY</li>
      <li>COLLAGEN AND ADVANCED DRESSINGS</li>
      <li>SURGICAL/ TRAUMA WOUNDS</li>
      <li>VENOUS/ ARTERIAL WOUNDS</li>
      <li>DEBRIDEMENTS</li>
    </ul>
  </div>

  <div class="panel p3">
    <h2 class="abs center heading" style="width:231px">PERSONALIZED<br>CARE PLANS</h2>
    <p class="abs body-copy" style="left:22px;top:124px;width:190px">Customized care plans designed to meet the specific needs of each patient, ensuring optimal healing. Coordination and direction of care for other caregivers and clinicians, including home health.Patient and Caregiver Education Providing education and support to patients and their caregivers to enhance understanding and promote self-care.</p>
    <div class="abs forest" role="img" aria-label="Misty evergreen forest photo in a circle" style="background:linear-gradient(180deg,#e8e6e0 0%,#a9b3ad 30%,#4d6358 60%,#26372f 100%)"></div>
    <p class="abs center brand-name" style="top:470px;width:231px;font-size:14px">Harbor Lane Care</p>
  </div>

  <div class="accent-band"></div>
</section>

</body>
</html>
```